Business Card Design

We are an IT staffing and consulting company providing IT solutions and resources to our clients.

Industry/Entity Type

Business

Contact Information for Business Card

Ravindra Kolluparthi
Vice President

BrimTrail Inc
48260 Hollyfern Market Court, suite 700
Larkfield, VT 05999
Direct: 571-555-0193
Mobile: 571-555-0147
Email: Ravindra@brimtrailinc.example
Fax: 703-555-0162
www.brimtrailinc.example

```html
<!DOCTYPE html>
<html lang="en">
<head>
<meta charset="utf-8">
<title>BrimTrail Inc — Business Card</title>
<link rel="stylesheet" href="https://fonts.googleapis.com/css2?family=Oswald:wght@500;600&family=Open+Sans:wdth,wght@75,300;75,400;100,300;100,400&display=swap">
<style>
  :root {
    --bg: #e9e7e3;
    --card: #ffffff;
    --ink: #1d1d1d;
    --band: #2b2b2c;
    --accent: #c0202b;
    --light: #f2f2f2;
    --muted: #444444;
  }
  * { margin: 0; padding: 0; box-sizing: border-box; }
  html, body { width: 1200px; height: 902px; overflow: hidden; background: var(--bg); }
  .stage { position: relative; width: 1200px; height: 902px; }
  .card {
    position: absolute; top: 301px; width: 520px; height: 300px;
    background: var(--card); border-radius: 18px; overflow: hidden;
    box-shadow: 0 10px 24px rgba(0,0,0,.18), 0 2px 4px rgba(0,0,0,.12);
  }
  .card--front { left: 50px; }
  .card--back { left: 630px; }

  .brand {
    position: absolute; left: 0; right: 0; top: 96px; text-align: center;
    font-family: "Open Sans", sans-serif; font-weight: 300; font-stretch: 100%;
    font-size: 56px; letter-spacing: 1px; color: var(--ink); line-height: 1;
  }
  .front-web {
    position: absolute; left: 0; right: 0; top: 196px; text-align: center;
    font-family: "Open Sans", sans-serif; font-weight: 300; font-stretch: 75%;
    font-size: 17px; color: var(--accent); letter-spacing: .3px;
  }

  .holder { position: absolute; left: 0; right: 0; top: 60px; text-align: center; }
  .holder__name {
    font-family: "Oswald", sans-serif; font-weight: 600; font-size: 24px;
    letter-spacing: .5px; text-transform: uppercase; line-height: 1; color: var(--ink);
  }
  .holder__first { color: var(--accent); }
  .holder__title {
    margin-top: 6px; font-family: "Open Sans", sans-serif; font-stretch: 75%;
    font-weight: 400; font-size: 15px; color: var(--muted);
  }

  .band {
    position: absolute; left: 0; right: 0; top: 170px; bottom: 0;
    background: var(--band);
    clip-path: polygon(0 0, 100% 0, 100% 100%, 0 100%);
  }
  .contact {
    position: absolute; top: 144px; width: 173px; text-align: center;
    font-family: "Open Sans", sans-serif; font-stretch: 75%; font-weight: 300;
    font-size: 13px; line-height: 1.65; color: var(--light);
  }
  .contact--web { left: 0; }
  .contact--phone { left: 173px; }
  .contact--place { left: 346px; }
  .contact__icon { display: block; margin: 0 auto 12px; width: 52px; height: 52px; }
  .contact__line { display: block; white-space: nowrap; }
</style>
</head>
<body>
<main class="stage">

  <section class="card card--front" aria-label="Card front">
    <div class="brand">BrimTrail</div>
    <div class="front-web">www.brimtrailinc.example</div>
  </section>

  <section class="card card--back" aria-label="Card back">
    <div class="holder">
      <div class="holder__name"><span class="holder__first">Ravindra</span> Kolluparthi</div>
      <div class="holder__title">Vice President</div>
    </div>

    <div class="band"></div>

    <div class="contact contact--web">
      <svg class="contact__icon" viewBox="0 0 52 52" aria-hidden="true">
        <circle cx="26" cy="26" r="24" fill="var(--band)" stroke="var(--light)" stroke-width="2"/>
        <g fill="none" stroke="var(--light)" stroke-width="1.4">
          <circle cx="26" cy="26" r="10"/>
          <ellipse cx="26" cy="26" rx="4.5" ry="10"/>
          <line x1="16" y1="26" x2="36" y2="26"/>
          <line x1="18" y1="20" x2="34" y2="20"/>
          <line x1="18" y1="32" x2="34" y2="32"/>
        </g>
      </svg>
      <span class="contact__line">Ravindra@brimtrailinc.example</span>
      <span class="contact__line">www.brimtrailinc.example</span>
    </div>

    <div class="contact contact--phone">
      <svg class="contact__icon" viewBox="0 0 52 52" aria-hidden="true">
        <circle cx="26" cy="26" r="24" fill="var(--band)" stroke="var(--light)" stroke-width="2"/>
        <rect x="19" y="15" width="14" height="22" rx="2.5" fill="none" stroke="var(--light)" stroke-width="1.6"/>
        <line x1="23" y1="33.5" x2="29" y2="33.5" stroke="var(--light)" stroke-width="1.4"/>
      </svg>
      <span class="contact__line">D:555-555-0193, M:555-555-0147</span>
      <span class="contact__line">F:555-555-0162</span>
    </div>

    <div class="contact contact--place">
      <svg class="contact__icon" viewBox="0 0 52 52" aria-hidden="true">
        <circle cx="26" cy="26" r="24" fill="var(--band)" stroke="var(--light)" stroke-width="2"/>
        <path d="M26 38 C20 30 18 27 18 23 a8 8 0 0 1 16 0 c0 4 -2 7 -8 15z" fill="none" stroke="var(--light)" stroke-width="1.6"/>
        <circle cx="26" cy="23" r="3" fill="none" stroke="var(--light)" stroke-width="1.4"/>
      </svg>
      <span class="contact__line">48260 Hollyfern Market Court,</span>
      <span class="contact__line">suite 700 Larkfield, VT 05999</span>
    </div>
  </section>

</main>
</body>
</html>
```